Create look and feel for existing Web Page

Update Web Page

We have a website at http://www.usekivra.com/index-web.html. It is a single page html site, with a custom signup form. We also have a quill bay plugin at the bottom of the page. We'd like to redesign the look and feel of the entire site. We sell software to eye doctors. Also called optometrists, our software tool makes it easy for doctors to manage patients, bill, and document patient encounters. I have included our logos below.

We are looking for a new design preferably in HTML 5, CSS etc. The fields on the form on this page: http://www.usekivra.com/index-web.html

You can get screen shots of our software application at this site: http://staging.usekivra.com
username: test@samplevora.com
password: password

```html
<!DOCTYPE html>
<html lang="en">
<head>
<meta charset="utf-8">
<title>Vistrell — Office operating system for optometrists</title>
<link rel="stylesheet" href="https://fonts.googleapis.com/css2?family=Montserrat:wght@400;500;600;700;800&display=swap">
<style>
:root{
  --orange:#f7821b;
  --orange-dark:#ec7410;
  --ink:#1c1c1c;
  --text:#222;
  --white:#fff;
  --page:#f6f6f6;
  --dark:#1e1e1e;
  --line:#d9d9d9;
}
*{margin:0;padding:0;box-sizing:border-box}
html,body{width:1200px;height:2705px;overflow:hidden}
body{font-family:"Montserrat",Arial,sans-serif;color:var(--text);background:var(--page);position:relative}
.abs{position:absolute}
.center{text-align:center;left:0;width:1200px}

/* hero */
.hero{position:absolute;left:0;top:0;width:1200px;height:608px;
  background:radial-gradient(ellipse at 55% 18%,#5a5a5a 0%,#3a3a3a 35%,#262626 75%,#1d1d1d 100%)}
.logo{font-family:"Montserrat",Arial,sans-serif;font-weight:500;color:var(--orange);letter-spacing:2px}
.hero .logo{left:155px;top:20px;font-size:30px}
.nav{position:absolute;top:32px;right:153px;display:flex;gap:33px;font-size:13px;font-weight:600;letter-spacing:1.3px;color:var(--white)}
.nav .active{color:var(--orange)}
.hero-title{top:254px;font-size:35px;font-weight:700;line-height:50px;color:var(--orange)}
.hero-text{top:366px;font-size:19.5px;line-height:29px;color:#eee;left:150px;width:900px;text-align:center}
.btn{display:flex;align-items:center;justify-content:center;font-weight:700;text-transform:uppercase}
.hero-btn{left:453px;top:456px;width:294px;height:50px;background:var(--orange);color:var(--white);font-size:12px}

/* features */
.eyebrow{font-size:15px;font-weight:500;color:var(--text);letter-spacing:.3px}
.features-eyebrow{top:639px}
.features-title{top:664px;font-size:33px;font-weight:700;color:var(--orange)}
.features-text{top:712px;font-size:17px;line-height:24px;color:#333}
.card{position:absolute;width:283px;height:253px;background:var(--white);box-shadow:0 1px 6px rgba(0,0,0,.1);text-align:center}
.card svg{position:absolute;left:108px;top:22px;width:68px;height:68px}
.card h3{position:absolute;top:110px;left:0;width:100%;font-size:23px;font-weight:700;color:var(--orange)}
.card p{position:absolute;top:160px;left:46px;width:191px;font-size:12.5px;line-height:14.5px;color:#222}

/* pricing */
.pricing-title{top:1372px;font-size:42px;font-weight:800;color:var(--ink)}
.pricing-title span{color:var(--orange)}
.rule{height:3px;background:var(--ink);top:1397px}
.plan{position:absolute;background:var(--white);border:1px solid #ddd;text-align:center}
.plan h4{font-size:25px;font-weight:700;color:var(--orange);margin-top:36px}
.plan .price{font-size:38px;font-weight:800;color:var(--ink);margin-top:18px;line-height:40px}
.plan .unit{font-size:16px;font-weight:600;color:var(--ink)}
.plan .divider{width:142px;height:1px;background:#777;margin:20px auto 0}
.plan .desc{font-size:20px;line-height:23px;color:var(--ink);margin:26px auto 0;width:210px}
.plan .btn{position:absolute;left:58px;width:168px;height:44px;background:var(--orange);color:var(--white);font-size:17px;text-transform:none}
.plan.featured{background:var(--orange);border:none;box-shadow:0 3px 8px rgba(0,0,0,.25)}
.plan.featured h4{color:var(--white);font-size:37px;margin-top:28px}
.plan.featured .price,.plan.featured .unit{color:var(--white)}
.plan.featured .divider{background:#fbd3ad}
.plan.featured .desc{color:var(--white);font-size:21px;width:230px;font-weight:500;margin-top:36px}
.plan.featured .btn{background:var(--white);color:var(--orange);left:54px;width:172px;height:48px;font-size:21px}

/* call to action band */
.cta{position:absolute;left:0;top:1998px;width:1200px;height:194px;
  background:linear-gradient(115deg,#f7831d 0%,#f48a2c 35%,#f27c16 65%,#f8862a 100%)}
.cta h2{position:absolute;top:46px;left:0;width:100%;text-align:center;color:var(--white);font-size:33px;font-weight:700}
.cta .btn{left:482px;top:116px;width:236px;height:48px;background:var(--white);color:var(--orange);font-size:16px}

/* waitlist */
.waitlist{position:absolute;left:0;top:2192px;width:1200px;height:513px;
  background:radial-gradient(ellipse at 30% 30%,#2e2e2e 0%,#1f1f1f 60%,#191919 100%)}
.waitlist .eyebrow{left:159px;top:87px;color:var(--white)}
.waitlist h2{left:155px;top:110px;font-size:33px;line-height:42px;font-weight:700;color:var(--orange)}
.waitlist p{left:155px;top:206px;width:400px;font-size:18px;line-height:31px;color:#eee}
.waitlist .logo{left:155px;top:318px;font-size:44px}
.follow{left:155px;top:403px;font-size:15px;font-weight:600;color:var(--white)}
.social{position:absolute;top:432px;width:32px;height:32px}
.field{position:absolute;left:635px;width:414px;height:52px;border:1px solid #555;background:rgba(0,0,0,.35);color:#ddd;font-size:17px;padding-left:19px;display:flex;align-items:center}
.waitlist .submit{left:741px;top:410px;width:308px;height:52px;background:var(--orange);color:var(--white);font-size:12.5px}
</style>
</head>
<body>

<header class="hero" role="img" aria-label="Dimmed photograph of an optometry exam room with a phoropter overhead">
  <div class="abs logo">vistrell</div>
  <nav class="nav">
    <span class="active">HOME</span><span>PRODUCTS</span><span>PRICING</span><span>SIGNUP</span><span>CONTACT</span>
  </nav>
  <h1 class="abs center hero-title">LEASE PRACTICES:<br>CHOOSE HOW YOU SPEND YOUR TIME</h1>
  <p class="abs hero-text">Vistrell is your office operating system. Automate your painful tasks, keep track of your books, and live a little. Start with a&nbsp; FREE charting tool and add more products as you grow.</p>
  <div class="abs btn hero-btn">Get the charting tool for free</div>
</header>

<section class="features">
  <div class="abs center eyebrow features-eyebrow">JOIN THE COOL CLUB</div>
  <h2 class="abs center features-title">AI TO AUTOMATE OPTOMETRY OFFICE TASKS</h2>
  <p class="abs center features-text">Vistrell uses AI, automation, robots, and other cool technology to streamline office work<br>so you can do things you love</p>

  <div class="card" style="left:154px;top:791px">
    <svg viewBox="0 0 68 68" fill="none" stroke="#f7821b" stroke-width="3"><rect x="3" y="8" width="52" height="46"/><line x1="3" y1="18" x2="55" y2="18"/><path d="M12 3v9M22 3v9M32 3v9M42 3v9M48 3v9"/><path d="M11 26h6M23 26h6M35 26h6M11 35h6M23 35h6M11 44h6M23 44h6"/><circle cx="50" cy="51" r="14" fill="#fff"/><path d="M50 43v8h6"/></svg>
    <h3>SCHEDULE</h3>
    <p>Meet your patients where they are, 24 hours 7 days a week with the online scheduler.</p>
  </div>
  <div class="card" style="left:459px;top:791px">
    <svg viewBox="0 0 68 68" fill="none" stroke="#f7821b" stroke-width="3"><circle cx="26" cy="26" r="14" stroke-dasharray="6 3"/><circle cx="26" cy="26" r="6"/><circle cx="50" cy="48" r="11" stroke-dasharray="5 3"/><circle cx="50" cy="48" r="4"/><circle cx="32" cy="56" r="6"/></svg>
    <h3>INTAKE</h3>
    <p>Never print out another paper form. Your patients are now able to fill out and sign forms online.</p>
  </div>
  <div class="card" style="left:764px;top:791px">
    <svg viewBox="0 0 68 68" fill="none" stroke="#f7821b" stroke-width="3"><path d="M6 14l8-8 48 48-8 8z"/><path d="M20 12l-4 4M28 20l-4 4M36 28l-4 4M44 36l-4 4"/><path d="M52 4l10 10-40 40-14 4 4-14z"/><path d="M46 10l10 10"/></svg>
    <h3>CHART</h3>
    <p>Start charting all patient findings for FREE. With features like auto population it flies on your mobile phone.</p>
  </div>
  <div class="card" style="left:154px;top:1069px">
    <svg viewBox="0 0 68 68" fill="none" stroke="#f7821b" stroke-width="3"><path d="M22 4h40v60H22"/><path d="M30 14h14M30 22h12M30 44h24M30 52h24"/><circle cx="52" cy="20" r="7"/><path d="M49 20l2 2 4-4"/><path d="M4 30h18l6 6-6 6H4z"/><path d="M30 38l18-10"/></svg>
    <h3>BILL</h3>
    <p>Don't waste your precious time or pay someone to bill insurance, let a bot do it for you.</p>
  </div>
  <div class="card" style="left:459px;top:1069px">
    <svg viewBox="0 0 68 68" fill="none" stroke="#f7821b" stroke-width="3.5"><path d="M16 14A26 26 0 0 1 58 24"/><path d="M52 52A26 26 0 0 1 10 44"/><path d="M58 12v12H46"/><path d="M10 56V44h12"/></svg>
    <h3>ELIGIBLE</h3>
    <p>Don't call or login into every insurance website to get patient eligibility and copays. Our bots do that too.</p>
  </div>
  <div class="card" style="left:764px;top:1069px">
    <svg viewBox="0 0 68 68" fill="none" stroke="#f7821b" stroke-width="3"><path d="M22 10h28a16 16 0 0 1 0 40H38l-4 12-6-12h-6a16 16 0 0 1 0-40z"/><path d="M18 26h34M18 32h34M18 38h34"/><path d="M10 4h6v8h-6zM20 4h6v8h-6z"/></svg>
    <h3>REVIEW</h3>
    <p>Grow your patient base and improve your search results with the review solution.</p>
  </div>
</section>

<section class="pricing">
  <div class="abs rule" style="left:329px;width:116px"></div>
  <div class="abs rule" style="left:757px;width:115px"></div>
  <h2 class="abs center pricing-title">OUR <span>PRICING</span></h2>

  <div class="plan" style="left:154px;top:1502px;width:282px;height:395px">
    <h4>Pick 1 Add one</h4>
    <div class="price">99$</div>
    <div class="unit">per location</div>
    <div class="divider"></div>
    <div class="desc">choose between schudles, intake, bill, eligle,or review</div>
    <div class="btn" style="top:306px">99$</div>
  </div>
  <div class="plan featured" style="left:460px;top:1464px;width:283px;height:460px">
    <h4>FREE</h4>
    <div class="price">0$</div>
    <div class="unit">per location</div>
    <div class="divider"></div>
    <div class="desc">chart patient finding for FREE unlimited users, doctors,and location</div>
    <div class="btn" style="top:374px">FREE</div>
  </div>
  <div class="plan" style="left:767px;top:1502px;width:282px;height:395px">
    <h4>Pick 2 Add one</h4>
    <div class="price">189$</div>
    <div class="unit">per location</div>
    <div class="divider"></div>
    <div class="desc" style="margin-top:16px">choose ant two between schudles, intake,bill,eligle,or review</div>
    <div class="btn" style="top:306px">99$</div>
  </div>
</section>

<section class="cta">
  <h2>Now spend time outside the office!</h2>
  <div class="abs btn">Join the club</div>
</section>

<section class="waitlist" role="img" aria-label="Dimmed photograph of an optometrist at work">
  <div class="abs eyebrow">GET ON THE WAITLIST</div>
  <h2 class="abs">GET STARTED WITH<br>A FREE CHARTING TOOL</h2>
  <p class="abs">Become part of a club that wants to change the way we practice, so we can have a life outside of the office.</p>
  <div class="abs logo">vistrell</div>
  <div class="abs follow">Follow us on</div>
  <span class="social" style="left:155px;background:#3b5a98"></span>
  <span class="social" style="left:206px;background:#5ab6e6"></span>
  <span class="social" style="left:257px;background:#4f74a3"></span>
  <span class="social" style="left:308px;background:#d9584a"></span>

  <div class="field" style="top:80px">Your Name</div>
  <div class="field" style="top:146px">Your Email</div>
  <div class="field" style="top:212px">Cell Phone</div>
  <div class="field" style="top:278px">Office Name</div>
  <div class="field" style="top:343px">NPI</div>
  <div class="abs btn submit">Get the charting tool for free</div>
</section>

</body>
</html>
```